Maritime Law Firm Business Card Design Project

We are a new maritime law firm starting in Queensland, Australia. The principal is a master mariner as well as a lawyer and is looking for a logo design that evokes a practical and user-friendly approach to the law, as well as maritime law expertise.

We would like to use the compass rose as the foundation for the design, as it symbolises clarity of direction and purpose, as well as traditional maritime heritage.

The 16th Century Luis Bercedo Compass Rose (attached) is beautiful, but is too complex for a logo. A simplified version is desired.

Colour Paletter s flexible, although a B&W version is also needed. Colour suggestions are navy blue (for the sea), red and green (navigation lights) and maroon (for Queensland).

Target Market(s)

Maritime Industry/legal services

Industry/Entity Type

Law Firm

Font styles to use
Sans Serif

Requirements
Must have
• Contact Details
Name of 'Pellworth Legal'

```html
<!DOCTYPE html>
<html lang="en">
<head>
<meta charset="UTF-8">
<title>Pellworth Legal – Business Card</title>
<link rel="stylesheet" href="https://fonts.googleapis.com/css2?family=Open+Sans:wght@400;600;700&display=swap">
<style>
  :root {
    --backdrop: #cbcbcb;
    --card-white: #ffffff;
    --navy: #0d1638;
    --navy-deep: #0a1230;
    --brand-navy: #0f1c5a;
    --green: #0e9146;
    --accent-red: #e2262c;
    --text-light: #ffffff;
  }
  * { margin: 0; padding: 0; box-sizing: border-box; }
  html, body {
    width: 1200px;
    height: 900px;
    overflow: hidden;
    background: var(--backdrop);
    font-family: "Open Sans", sans-serif;
  }
  .business-card {
    position: absolute;
    left: 160px;
    top: 165px;
    width: 880px;
    height: 570px;
    border-radius: 40px;
    overflow: hidden;
    background: var(--card-white);
    box-shadow: 0 18px 40px rgba(0,0,0,0.25);
  }
  .brand-area {
    position: absolute;
    left: 0; top: 0;
    width: 100%;
    height: 280px;
    display: flex;
    align-items: center;
    padding-left: 56px;
    gap: 28px;
  }
  .brand-mark {
    width: 120px;
    height: 120px;
    border-radius: 50%;
    background: var(--brand-navy);
    flex-shrink: 0;
  }
  .brand-name {
    font-size: 66px;
    font-weight: 400;
    color: var(--brand-navy);
    letter-spacing: 0.5px;
  }
  .divider-band {
    position: absolute;
    left: 0; top: 280px;
    width: 100%;
    height: 14px;
    background: var(--green);
  }
  .contact-area {
    position: absolute;
    left: 0; top: 294px;
    width: 100%;
    height: 276px;
    background: linear-gradient(180deg, var(--navy) 0%, var(--navy-deep) 100%);
    padding: 30px 0 0 56px;
    color: var(--text-light);
  }
  .person-name {
    font-size: 30px;
    font-weight: 700;
    color: var(--accent-red);
    line-height: 1.1;
  }
  .person-role {
    font-size: 19px;
    font-weight: 400;
    margin-top: 4px;
  }
  .contact-list {
    list-style: none;
    margin-top: 24px;
  }
  .contact-item {
    display: flex;
    align-items: center;
    gap: 14px;
    font-size: 21px;
    font-weight: 600;
    line-height: 32px;
  }
  .contact-icon {
    width: 20px;
    height: 20px;
    fill: var(--accent-red);
    flex-shrink: 0;
  }
</style>
</head>
<body>
  <div class="business-card">
    <header class="brand-area">
      <div class="brand-mark"></div>
      <div class="brand-name">Pellworth Legal</div>
    </header>
    <div class="divider-band"></div>
    <section class="contact-area">
      <div class="person-name">DANA WHITLOW</div>
      <div class="person-role">Manager</div>
      <ul class="contact-list">
        <li class="contact-item">
          <svg class="contact-icon" viewBox="0 0 24 24" aria-hidden="true"><path d="M6.6 10.8a15.1 15.1 0 0 0 6.6 6.6l2.2-2.2c.3-.3.7-.4 1-.2 1.1.4 2.3.6 3.6.6.6 0 1 .4 1 1V20c0 .6-.4 1-1 1A17 17 0 0 1 3 4c0-.6.4-1 1-1h3.5c.6 0 1 .4 1 1 0 1.3.2 2.5.6 3.6.1.3 0 .7-.2 1z"/></svg>
          <span>0482 316 908</span>
        </li>
        <li class="contact-item">
          <svg class="contact-icon" viewBox="0 0 24 24" aria-hidden="true"><path d="M7 2h10a1 1 0 0 1 1 1v18a1 1 0 0 1-1 1H7a1 1 0 0 1-1-1V3a1 1 0 0 1 1-1zm1 3v6h8V5zm0 8v2h2v-2zm3 0v2h2v-2zm3 0v2h2v-2zm-6 3v2h2v-2zm3 0v2h2v-2zm3 0v2h2v-2z"/></svg>
          <span>0417 285 462</span>
        </li>
        <li class="contact-item">
          <svg class="contact-icon" viewBox="0 0 24 24" aria-hidden="true"><path d="M2 6a1 1 0 0 1 1-1h18a1 1 0 0 1 1 1v12a1 1 0 0 1-1 1H3a1 1 0 0 1-1-1zm2 1.2v.3l8 5.2 8-5.2v-.3z"/></svg>
          <span>info@pellworthlegal.com</span>
        </li>
        <li class="contact-item">
          <svg class="contact-icon" viewBox="0 0 24 24" aria-hidden="true"><path d="M12 3l10 9h-3v9h-5v-6h-4v6H5v-9H2z"/></svg>
          <span>po box, harbour lane, Queensland</span>
        </li>
      </ul>
    </section>
  </div>
</body>
</html>
```